Lead Sales Portal Needs to Generate B2B Signup's

We are looking for banner ad designs to drive new business (B2B) traffic to our insurance and mortgage industry self serve lead sites. The sites are HomeLoanProspectHub.com and CoverageProspectHub.com, and we service over 45,000 insurance agents and mortgage lenders in a self serve lead portal model. We want our banners to generate more of these clients.

Our clients come to our sites, browse our database and then pick out and purchase the consumer leads that they need to generate new business.

We advertise extensively on Zorvix and on other PPC platforms, and our existing banners are looking really tired.

Some of the ad copy that works well for us is:

Cherry Pick Your Life Leads - Why Pay More Than $3.50 For Life Insurance Leads?
Sign up today and we'll match up to $250

Agents - Here's $250 For New Clients. Cherry Pick Your Life Insurance Leads & Save! Sign up today and we'll match up to $250

One of our Landing Pages that performs well is here:
http://www.coverageprospecthub.com/lp/008/

One of our competitors ad's are here:

http://www.tralvo.com/search/results?q=PolicyBeacon&ad=427360

We're looking for a design that is eye catching, uses our "Deeply Discounted Leads" and our "$250 match bonus"

This is the second contest that we have for the same sites. The previous designs were great and really performed well, so we are looking for new designs now that 6 months have passed. I have uploaded some winning banners from the last group for your information.
Updates

Project Deadline Extended
Reason: I've been asked by some of the designers to delay a day to get their designs in. I'm happy to do it!

Target Market(s)

These are insurance agents and mortgage lenders. All of our clients are business' or individuals within the business. This is a B2B campaign, so we need something that is professional and upscale. These are NOT consumer facing ad's!

Industry/Entity Type

Insurance

Font styles to use
Sans Serif

Requirements
Must have
• We must have the logos for the sites in the banners. Also, we must have a call to action arrow and "Go" button. Some animation is necessary, (especially around the arrow and the GO button).

One or two designs.

File type

.JPEG
.JPG
.PNG
.GIF

File size

150 KB or smaller

Image sizes

Vertical rectangle: 240 x 400
Mobile leaderboard: 320 x 50
Banner: 468 x 60
Leaderboard: 728 x 90
Square: 250 x 250
Small square: 200 x 200
Large rectangle: 336 x 280
Inline rectangle: 300 x 250
Skyscraper: 120 x 600
Wide skyscraper: 160 x 600
Half-page: 300 x 600
Large leaderboard: 970 x 90

```html
<!DOCTYPE html>
<html lang="en">
<head>
<meta charset="utf-8">
<title>Coverage Prospect Hub – Banner Set</title>
<link rel="stylesheet" href="https://fonts.googleapis.com/css2?family=Arimo:wght@400;700&display=swap">
<style>
  :root {
    --page: #ffffff;
    --ink: #222222;
    --label: #444444;
    --size-note: #f05a1a;
    --orange: #f08a12;
    --dark-1: #0e0e0e;
    --dark-2: #3b3b3b;
    --green-1: #b3dd3a;
    --green-2: #5c980e;
    --green-text: #3f6b06;
    --header-1: #ffffff;
    --header-2: #d9d9d9;
    --photo-1: #e9e6e3;
    --photo-2: #6e6a66;
    --btn-1: #5a5a5a;
    --btn-2: #151515;
    --white: #ffffff;
  }
  * { box-sizing: border-box; margin: 0; padding: 0; }
  html, body { width: 1200px; height: 1200px; overflow: hidden; background: var(--page); }
  body { font-family: "Arimo", Arial, sans-serif; }
  .sheet { position: absolute; left: 0; top: 0; width: 850px; height: 850px; transform: scale(1.41176); transform-origin: 0 0; }

  .banner { position: absolute; overflow: hidden; border: 1px solid #9a9a9a; background: var(--dark-1); }
  .layer { position: absolute; }
  .header { background: linear-gradient(var(--header-1), var(--header-2)); }
  .dark { background: linear-gradient(135deg, var(--dark-1), var(--dark-2) 60%, var(--dark-1)); }
  .green { background: linear-gradient(var(--green-1), var(--green-2)); }
  .photo { background: radial-gradient(circle at 40% 45%, var(--photo-1), var(--photo-2)); }
  .arcs { position: absolute; left: 0; top: 0; }

  .brand { position: absolute; display: flex; align-items: center; gap: 4px; color: var(--ink); font-size: 12px; font-weight: 400; white-space: nowrap; }
  .brand-dot { width: 18px; height: 18px; border-radius: 50%; background: var(--ink); flex: none; }

  .headline { position: absolute; color: var(--white); font-weight: 700; text-align: center; line-height: 1.08; text-shadow: 0 1px 2px #000; }
  .offer-box { position: absolute; border-radius: 4px; background: linear-gradient(var(--green-1), var(--green-2)); border: 1px solid #d6f27a; color: var(--green-text); font-weight: 700; text-align: center; line-height: 1.05; display: flex; align-items: center; justify-content: center; padding: 4px 8px; text-shadow: 0 1px 0 #d8f38c; }
  .match-note { position: absolute; color: var(--white); font-weight: 700; text-align: center; line-height: 1.05; text-shadow: 0 1px 2px #2d4a04; }

  .cta { position: absolute; border-radius: 4px; background: linear-gradient(var(--btn-1), var(--btn-2)); border: 1px solid #777; box-shadow: 0 2px 3px rgba(0,0,0,.4); color: var(--white); font-weight: 700; font-size: 17px; display: flex; align-items: center; justify-content: space-between; padding: 0 8px 0 26px; }
  .cta-arrow { width: 26px; height: 26px; border-radius: 50%; background: #000; display: flex; align-items: center; justify-content: center; }

  .caption { position: absolute; font-size: 15px; color: var(--label); white-space: nowrap; }
  .caption .weight { color: var(--size-note); margin-left: 6px; }
</style>
</head>
<body>
<main class="sheet">

  <!-- Leaderboard 728 x 90 -->
  <section class="banner leaderboard" style="left:55px;top:33px;width:728px;height:90px;">
    <div class="layer header" style="left:0;top:0;width:205px;height:90px;"></div>
    <div class="layer photo" role="img" aria-label="Photo of two smiling business professionals" style="left:175px;top:0;width:120px;height:90px;"></div>
    <div class="layer dark" style="left:290px;top:0;width:290px;height:90px;"></div>
    <div class="layer green" style="left:560px;top:0;width:168px;height:90px;"></div>
    <svg class="arcs" width="728" height="90" viewBox="0 0 728 90" aria-hidden="true">
      <path d="M192 0 Q162 45 192 90" fill="none" stroke="var(--orange)" stroke-width="6"/>
      <path d="M288 0 Q300 45 288 90" fill="none" stroke="#cfcfcf" stroke-width="3"/>
      <path d="M552 0 Q590 45 552 90" fill="none" stroke="var(--orange)" stroke-width="7"/>
    </svg>
    <div class="brand" style="left:6px;top:35px;"><span class="brand-dot"></span>Coverage Prospect Hub</div>
    <p class="headline" style="left:296px;top:14px;width:108px;font-size:17px;">Cherry Pick Your Life Leads</p>
    <p class="offer-box" style="left:405px;top:15px;width:145px;height:62px;font-size:13px;">Why Pay More Than $3.5 for Life Insurance Leads?</p>
    <p class="match-note" style="left:563px;top:6px;width:162px;font-size:14px;">Sign Up Today &amp; We'll Make up To $250</p>
    <div class="cta" style="left:578px;top:46px;width:140px;height:36px;">Sign Up
      <span class="cta-arrow"><svg width="10" height="12" viewBox="0 0 10 12"><path d="M1 0 L10 6 L1 12Z" fill="#fff"/></svg></span>
    </div>
  </section>
  <p class="caption" style="left:55px;top:132px;">728X90<span class="weight">23.8 KB</span></p>

  <!-- Inline rectangle 300 x 250 -->
  <section class="banner rectangle" style="left:53px;top:219px;width:300px;height:250px;">
    <div class="layer header" style="left:0;top:0;width:300px;height:60px;"></div>
    <div class="layer dark" style="left:0;top:55px;width:300px;height:140px;"></div>
    <div class="layer photo" role="img" aria-label="Photo of two smiling business professionals" style="left:175px;top:42px;width:125px;height:150px;"></div>
    <div class="layer green" style="left:0;top:185px;width:300px;height:65px;"></div>
    <svg class="arcs" width="300" height="250" viewBox="0 0 300 250" aria-hidden="true">
      <path d="M0 62 Q120 38 300 48" fill="none" stroke="var(--orange)" stroke-width="7"/>
      <path d="M190 48 Q160 120 200 190" fill="none" stroke="#d8d8d8" stroke-width="3"/>
      <path d="M0 185 Q150 170 300 182" fill="none" stroke="var(--orange)" stroke-width="8"/>
    </svg>
    <div class="brand" style="left:76px;top:12px;font-size:14px;"><span class="brand-dot" style="width:22px;height:22px;"></span>Coverage Prospect Hub</div>
    <p class="headline" style="left:13px;top:78px;width:146px;font-size:19px;">Cherry Pick Your Life Leads</p>
    <p class="offer-box" style="left:8px;top:125px;width:152px;height:66px;font-size:13px;">Why Pay More Than $3.5 for Life Insurance Leads?</p>
    <div class="cta" style="left:15px;top:206px;width:142px;height:37px;">Sign Up
      <span class="cta-arrow"><svg width="10" height="12" viewBox="0 0 10 12"><path d="M1 0 L10 6 L1 12Z" fill="#fff"/></svg></span>
    </div>
    <p class="match-note" style="left:172px;top:202px;width:118px;font-size:13px;">Sign Up Today &amp; We'll Make up To $250</p>
  </section>
  <p class="caption" style="left:53px;top:478px;">300X250<span class="weight">27.5 KB</span></p>

  <!-- Wide skyscraper 160 x 600 -->
  <section class="banner skyscraper" style="left:620px;top:168px;width:160px;height:600px;">
    <div class="layer header" style="left:0;top:0;width:160px;height:85px;"></div>
    <div class="layer photo" role="img" aria-label="Photo of two smiling business professionals" style="left:0;top:78px;width:160px;height:190px;"></div>
    <div class="layer dark" style="left:0;top:262px;width:160px;height:210px;"></div>
    <div class="layer green" style="left:0;top:465px;width:160px;height:135px;"></div>
    <svg class="arcs" width="160" height="600" viewBox="0 0 160 600" aria-hidden="true">
      <path d="M0 100 Q80 62 160 100" fill="none" stroke="var(--orange)" stroke-width="7"/>
      <path d="M0 262 Q80 250 160 268" fill="none" stroke="#d8d8d8" stroke-width="3"/>
      <path d="M0 468 Q80 448 160 468" fill="none" stroke="var(--orange)" stroke-width="9"/>
    </svg>
    <div class="brand" style="left:8px;top:31px;font-size:11px;"><span class="brand-dot"></span>Coverage Prospect Hub</div>
    <p class="headline" style="left:4px;top:272px;width:152px;font-size:25px;">Cherry Pick Your Life Leads</p>
    <p class="offer-box" style="left:10px;top:360px;width:140px;height:104px;font-size:16px;">Receive $250 Worth Of Leads Today by Just Sign Up</p>
    <p class="match-note" style="left:10px;top:489px;width:140px;font-size:16px;">Sign Up Today &amp; We'll Make up To $250</p>
    <div class="cta" style="left:8px;top:552px;width:144px;height:40px;">Sign Up
      <span class="cta-arrow"><svg width="10" height="12" viewBox="0 0 10 12"><path d="M1 0 L10 6 L1 12Z" fill="#fff"/></svg></span>
    </div>
  </section>
  <p class="caption" style="left:628px;top:776px;">160X600<span class="weight">33.9 KB</span></p>

</main>
</body>
</html>
```